WP website design (Valmond)

We need a wordpress design for an established auction and real estate company based in Kansas. The winning design will incorporate a professional color scheme with company logo in a clean layout. The design needs to consider that this will be developed on a responsive theme. Colors are blue and gray, with perhaps an accent/highlight color.

• Navigation:
1) Home 2) Auctions 3) Real Estate Listings 4) Buyers 5) Sellers 6) About Us 7) Contact Us 7) Brokers

Page will have slideshow, please use any stock real estate image initially. Homepage will have auctions - as at http://brindlegavelhouse.example/upcoming-auctions/. Footer will have smaller company logo and attached association logos.

Widgets:
1) email sign up 2) Social media (twitter, FB, youtube, RSS) 3) News & Events blog 4) Video Player
• demonstrate the drop-down menu styling, Past Auctions - under the main Auctions tab

```html
<!DOCTYPE html>
<html lang="en">
<head>
<meta charset="utf-8">
<title>Prairie Crest – Valmond Auction/Realty, LLC</title>
<link href="https://fonts.googleapis.com/css2?family=Tinos:wght@400;700&family=Open+Sans:wght@400;600&display=swap" rel="stylesheet">
<style>
:root{
  --blue:#245a8e;
  --blue-dark:#16406b;
  --blue-deep:#0f3a66;
  --blue-bright:#1b7fd6;
  --ink:#2f3f52;
  --text:#555;
  --muted:#8a8a8a;
  --line:#cfcfcf;
  --panel:#fafafa;
  --gray-bg:#e6e6e6;
  --dark:#2c2c2c;
  --white:#fff;
}
*{box-sizing:border-box;margin:0;padding:0}
html,body{width:1200px;height:2222px;overflow:hidden}
body{position:relative;font-family:"Tinos",serif;color:var(--text);background:linear-gradient(#f3f3f3 0,#eaeaea 700px,#e0e0e0 1819px)}
.abs{position:absolute}

/* header */
.site-header{position:absolute;left:0;top:0;width:1200px;height:145px;background:#f4f4f4}
.brand{position:absolute;left:67px;top:30px;width:200px;text-align:center;color:var(--blue-dark)}
.brand-name{font-size:32px;font-weight:700;line-height:1}
.brand-sub{font-size:15px;color:#777;line-height:1.2;margin-top:6px;font-family:"Open Sans",sans-serif}
.social{position:absolute;left:1003px;top:49px;display:flex;gap:5px}
.social span{width:31px;height:31px;display:block}
.search{position:absolute;left:951px;top:92px;width:194px;height:34px;border:1px solid #b7c4d2;background:#fff}
.search span{position:absolute;left:10px;top:9px;font-family:"Open Sans",sans-serif;font-size:12px;color:#9aa}
.search button{position:absolute;right:-1px;top:-1px;width:45px;height:34px;border:0;background:var(--blue-dark)}
.main-nav{position:absolute;left:0;top:145px;width:1200px;height:55px;background:var(--blue);border-bottom:2px solid var(--blue-dark)}
.main-nav ul{list-style:none;display:flex;justify-content:space-between;padding:0 45px 0 62px;line-height:55px}
.main-nav li{color:#fff;font-size:14px;letter-spacing:1.2px}

/* hero */
.hero{position:absolute;left:47px;top:216px;width:1106px;height:488px;background:#d9d9d9;border:1px solid #c5c5c5;border-radius:6px}
.hero-photo{position:absolute;left:9px;top:9px;width:1088px;height:471px;border-radius:5px;background:linear-gradient(180deg,#7fa9d6 0,#b9d2ea 35%,#e8dfc8 55%,#8d8a80 80%,#4c4c4c 100%)}
.hero-panel{position:absolute;left:9px;top:9px;width:1088px;height:471px;border-radius:5px;background:linear-gradient(160deg,#1e5a99,#0e3c6e);clip-path:polygon(670px 0,100% 0,100% 100%,545px 100%)}
.hero-band{position:absolute;left:699px;top:289px;width:446px;height:24px;background:#fff;color:var(--blue-dark);font-size:18px;letter-spacing:1px;padding-left:36px;line-height:24px}
.hero-title{position:absolute;left:735px;top:318px;color:#fff;font-size:46px;letter-spacing:2px}
.hero-text{position:absolute;left:741px;top:380px;width:390px;color:#eef4fb;font-size:16px;line-height:19px;letter-spacing:.4px}
.hero-text p+p{margin-top:19px}
.btn{position:absolute;height:37px;line-height:35px;text-align:center;font-size:15px;letter-spacing:.6px}
.btn-outline{border:1px solid #cfe0f2;color:#fff}
.btn-bright{background:var(--blue-bright);color:#fff;border:1px solid #1874c4}
.dots{position:absolute;left:1019px;top:651px;display:flex;gap:10px}
.dots span{width:14px;height:14px;border-radius:50%;background:#c8d6e6;border:2px solid #9fb8d2}
.dots span:first-child{background:var(--blue-bright)}

/* auctions */
.section-title{position:absolute;left:52px;top:772px;font-size:23px;letter-spacing:1.5px;color:#444}
.section-title b{color:var(--blue-dark);font-weight:700}
.section-rule{position:absolute;left:340px;top:786px;width:497px;height:1px;background:#d0d0d0}
.auction{position:absolute;left:53px;width:784px;height:240px}
.auction-photo{position:absolute;left:0;top:0;width:319px;height:181px;border:3px solid #d6d6d6;background:linear-gradient(180deg,#5f8cc2 0,#a7c3de 30%,#d8cf9f 50%,#4f7a3a 75%,#9fc2c9 100%)}
.auction-info{position:absolute;left:338px;top:-3px;width:446px;height:125px;background:var(--panel);border:1px solid #e1e1e1;padding:10px 12px}
.auction-title{font-size:21px;color:#333;letter-spacing:.4px}
.auction-desc{font-size:14px;line-height:18px;color:#666;margin-top:3px}
.auction-dates{position:absolute;left:338px;top:131px;width:446px;height:47px;background:var(--panel);border:1px solid #e1e1e1;padding:5px 10px;font-size:14px;line-height:19px;color:#555;letter-spacing:.5px}
.auction-dates b{font-weight:400;color:var(--blue);display:inline-block;width:64px}
.btn-details{left:0;top:194px;width:154px;height:40px;line-height:38px;border:2px solid #cfcfcf;background:#f4f4f4;color:#777;font-size:14px;letter-spacing:1.5px}
.btn-video{left:165px;top:194px;width:152px;height:40px;line-height:40px;background:var(--blue);color:#fff;font-size:14px;letter-spacing:1.5px}
.location{position:absolute;left:338px;top:194px;width:446px;height:40px;background:var(--blue);color:#fff;font-size:15px;line-height:40px;letter-spacing:.8px}
.location-label{position:absolute;left:0;top:0;width:120px;height:40px;background:var(--dark);clip-path:polygon(0 0,100% 0,88% 100%,0 100%);padding-left:26px}
.location-text{position:absolute;left:136px}
.btn-all{left:56px;top:1659px;width:205px;height:43px;line-height:43px;background:var(--blue);color:#fff;font-family:"Open Sans",sans-serif;font-size:15px;letter-spacing:1px;border-radius:2px}
.all-rule{position:absolute;left:272px;top:1681px;width:565px;height:1px;background:#cfcfcf}

/* sidebar */
.widget-head{position:absolute;left:881px;width:260px;height:42px;background:var(--blue-dark);border-radius:3px;color:#fff;font-size:18px;letter-spacing:1.5px;line-height:42px}
.widget-head .tab{position:absolute;left:0;top:0;width:82px;height:42px;background:#555;clip-path:polygon(0 0,100% 0,80% 100%,0 100%)}
.widget-head .icon{position:absolute;left:22px;top:12px;width:26px;height:18px;border:2px solid #ccc;border-radius:2px}
.widget-head .label{position:absolute;left:110px}
.about-photo{position:absolute;left:881px;top:856px;width:260px;height:125px;border:3px solid #d8d8d8;background:linear-gradient(180deg,#eef2f6,#c9d2de 60%,#3a3f48)}
.side-text{position:absolute;left:881px;width:260px;font-size:15px;line-height:18px;color:#555;letter-spacing:.3px}
.link{color:var(--blue-bright);font-size:16px;letter-spacing:.6px}
.post{position:absolute;left:889px;width:255px;height:173px;background:#dcdcdc;border:1px solid #cfcfcf;padding:12px 10px}
.post-thumb{position:absolute;left:10px;top:12px;width:70px;height:65px;border:3px solid #fff;background:linear-gradient(135deg,#e9eef3,#9aa5b2)}
.post-title{position:absolute;left:88px;top:16px;font-size:17px;color:var(--blue-dark)}
.post-text{position:absolute;left:10px;top:40px;width:238px;text-indent:78px;font-size:16px;line-height:18px;color:#666;letter-spacing:.4px}
.post-btn{position:absolute;left:9px;top:122px;width:92px;height:28px;background:var(--blue-dark);color:#fff;font-family:"Open Sans",sans-serif;font-size:12px;line-height:28px;text-align:center;border-radius:2px}
.view-all{position:absolute;left:899px;top:1576px;font-family:"Open Sans",sans-serif;font-size:14px;color:var(--muted);text-decoration:underline;letter-spacing:1px}
.newsletter{position:absolute;left:887px;top:1618px;width:255px;height:126px;background:linear-gradient(#e8e8e8,#cfcfcf);border:1px solid #c4c4c4;border-radius:3px}
.newsletter h3{position:absolute;left:21px;top:14px;font-weight:400;font-size:17px;letter-spacing:1.5px;color:var(--blue-dark)}
.newsletter .field{position:absolute;left:24px;top:46px;width:197px;height:31px;background:#fff;border:1px solid #cfcfcf;font-family:"Open Sans",sans-serif;font-size:14px;color:#aaa;padding:5px 8px}
.newsletter .submit{position:absolute;left:24px;top:84px;width:102px;height:31px;background:var(--blue);color:#fff;font-family:"Open Sans",sans-serif;font-size:14px;line-height:31px;text-align:center;letter-spacing:1px}

/* partners */
.partners{position:absolute;left:0;top:1819px;width:1200px;height:163px;background:#f5f5f5}
.badge{position:absolute;background:#3a3a3a}

/* footer */
.site-footer{position:absolute;left:0;top:1982px;width:1200px;height:199px;background:linear-gradient(#1f5188,#15406f)}
.foot-head{position:absolute;top:30px;color:#fff;font-size:19px;letter-spacing:2px;padding-bottom:8px;border-bottom:1px solid #6b8db3}
.foot-links{position:absolute;top:76px;list-style:none;font-family:"Open Sans",sans-serif;font-size:14px;color:#fff;letter-spacing:.8px;line-height:26px}
.foot-links li::before{content:"›";margin-right:8px;font-weight:600}
.foot-brand{position:absolute;left:855px;top:30px;width:162px;text-align:center;color:#c9d6e4}
.foot-brand .name{font-size:26px;font-weight:700;line-height:1}
.foot-brand .sub{font-size:13px;margin-top:6px;line-height:1.25;font-family:"Open Sans",sans-serif;color:#b7c8da}
.foot-social{position:absolute;left:866px;top:138px;display:flex;gap:8px}
.foot-social span{width:31px;height:31px;border-radius:50%;background:#d6dde5}
.copyright{position:absolute;left:0;top:2181px;width:1200px;height:41px;background:var(--dark);color:#ccc;font-size:13px;line-height:41px;padding-left:178px;letter-spacing:.8px}
</style>
</head>
<body>

<header class="site-header">
  <div class="brand">
    <div class="brand-name">Prairie Crest</div>
    <div class="brand-sub">Valmond<br>Auction/Realty, LLC</div>
  </div>
  <div class="social" aria-label="Social links">
    <span style="background:#5ab4e8"></span>
    <span style="background:#3b5f9e"></span>
    <span style="background:#e0452f"></span>
    <span style="background:#f39a1e"></span>
  </div>
  <div class="search">
    <span>SEARCH</span>
    <button aria-label="Search">
      <svg width="22" height="22" viewBox="0 0 22 22"><circle cx="9" cy="9" r="6" fill="none" stroke="#fff" stroke-width="2.5"/><line x1="13.5" y1="13.5" x2="19" y2="19" stroke="#fff" stroke-width="3.5" stroke-linecap="round"/></svg>
    </button>
  </div>
</header>

<nav class="main-nav">
  <ul>
    <li>HOME</li><li>AUCTIONS</li><li>REAL ESTATE LISTINGS</li><li>BUYERS</li><li>SELLERS</li><li>ABOUT US</li><li>CONTACT US</li><li>BROKERS</li>
  </ul>
</nav>

<section class="hero">
  <div class="hero-photo" role="img" aria-label="Stock photo of a large cream-sided two-storey house with dormers under a blue sky"></div>
  <div class="hero-panel"></div>
</section>
<div class="hero-band">Welcome to</div>
<h1 class="hero-title" style="font-weight:400">Prairie Crest</h1>
<div class="hero-text">
  <p>Praesent vulputate accumsan nulla. Cum sociis natoque penatibus et magnis dis parturient montes, nascetur ridiculus mus. Sed dapibus neque eget nulla dignissim.</p>
  <p>&nbsp;sit amet venenatis tortor blandit. Sed eget diam ipsum. Ut sed leo orci. Integer posuere ante diam, ac viverra diam vulputate non.</p>
</div>
<div class="btn btn-outline" style="left:744px;top:550px;width:166px">Read more</div>
<div class="btn btn-bright" style="left:918px;top:550px;width:168px">Auctions</div>
<div class="dots"><span></span><span></span><span></span></div>

<h2 class="section-title" style="font-weight:400"><b>UPCOMING</b> AUCTIONS</h2>
<div class="section-rule"></div>

<article class="auction" style="top:807px">
  <div class="auction-photo" role="img" aria-label="Photo of a Mediterranean-style villa with a pool and sun loungers"></div>
  <div class="auction-info">
    <h3 class="auction-title" style="font-weight:400">Title of the place goes here</h3>
    <p class="auction-desc">Maecenas at orci quis leo gravida rhoncus eu et nulla. Vestibulum ante ipsum primis in faucibus orci luctus et ultrices posuere cubilia Curae; Nam diam nisi, faucibus ut dui in, orci luctus et ultrices posuere cubilia Curae;</p>
  </div>
  <div class="auction-dates"><b>Begins:</b>Tuesday, March 04, 2014 at 10:00 AM EST<br><b>Ends:</b>Tuesday, March 11, 2014 at 11:00 PM EST</div>
  <div class="btn btn-details">VIEW DETAILS</div>
  <div class="btn btn-video">WATCH VIDEO</div>
  <div class="location"><span class="location-label">Location:</span><span class="location-text">P.O. Box 41027 Millbrook, KS 67210</span></div>
</article>

<article class="auction" style="top:1088px">
  <div class="auction-photo" role="img" aria-label="Photo of a Mediterranean-style villa with a pool and sun loungers"></div>
  <div class="auction-info">
    <h3 class="auction-title" style="font-weight:400">Title of the place goes here</h3>
    <p class="auction-desc">Maecenas at orci quis leo gravida rhoncus eu et nulla. Vestibulum ante ipsum primis in faucibus orci luctus et ultrices posuere cubilia Curae; Nam diam nisi, faucibus ut dui in, orci luctus et ultrices posuere cubilia Curae;</p>
  </div>
  <div class="auction-dates"><b>Begins:</b>Tuesday, March 04, 2014 at 10:00 AM EST<br><b>Ends:</b>Tuesday, March 11, 2014 at 11:00 PM EST</div>
  <div class="btn btn-details">VIEW DETAILS</div>
  <div class="btn btn-video">WATCH VIDEO</div>
  <div class="location"><span class="location-label">Location:</span><span class="location-text">P.O. Box 41027 Millbrook, KS 67210</span></div>
</article>

<article class="auction" style="top:1368px">
  <div class="auction-photo" role="img" aria-label="Photo of a Mediterranean-style villa with a pool and sun loungers"></div>
  <div class="auction-info">
    <h3 class="auction-title" style="font-weight:400">Title of the place goes here</h3>
    <p class="auction-desc">Maecenas at orci quis leo gravida rhoncus eu et nulla. Vestibulum ante ipsum primis in faucibus orci luctus et ultrices posuere cubilia Curae; Nam diam nisi, faucibus ut dui in, orci luctus et ultrices posuere cubilia Curae;</p>
  </div>
  <div class="auction-dates"><b>Begins:</b>Tuesday, March 04, 2014 at 10:00 AM EST<br><b>Ends:</b>Tuesday, March 11, 2014 at 11:00 PM EST</div>
  <div class="btn btn-details">VIEW DETAILS</div>
  <div class="btn btn-video">WATCH VIDEO</div>
  <div class="location"><span class="location-label">Location:</span><span class="location-text">P.O. Box 41027 Millbrook, KS 67210</span></div>
</article>

<div class="btn btn-all">VIEW ALL AUCTIONS</div>
<div class="all-rule"></div>

<aside>
  <div class="widget-head" style="top:807px"><span class="tab"><span class="icon"></span></span><span class="label">ABOUT US</span></div>
  <div class="about-photo" role="img" aria-label="Team photo of the agency staff in business suits"></div>
  <p class="side-text" style="top:990px">Lorem ipsum dolor sitamet, ect ipiscing elit. Quisque non elit sit amet lorem ut luctus faucibus non elit.</p>
  <p class="side-text" style="top:1072px">Lorem ipsum dolor sitamet, ect ipiscing elit. Quisque non elit sit amet lorem.</p>
  <span class="abs link" style="left:884px;top:1132px">Read more</span>

  <div class="widget-head" style="top:1166px"><span class="tab"><span class="icon"></span></span><span class="label">BLOG UPDATE</span></div>
  <div class="post" style="top:1215px">
    <div class="post-thumb" role="img" aria-label="Blog thumbnail of a presenter at a whiteboard"></div>
    <div class="post-title">Title of post here</div>
    <p class="post-text">ipsum dolor sit amet, consectetur taciti sociosqu ad litora tor per conubia nostra, pertos himenaeos</p>
    <div class="post-btn">Read More</div>
  </div>
  <div class="post" style="top:1394px">
    <div class="post-thumb" role="img" aria-label="Blog thumbnail of interlocking gears"></div>
    <div class="post-title">Title of post here</div>
    <p class="post-text">ipsum dolor sit amet, consectetur taciti sociosqu ad litora tor per conubia nostra, pertos himenaeos</p>
    <div class="post-btn">Read More</div>
  </div>
  <span class="view-all">VIEW ALL »</span>

  <div class="newsletter">
    <svg class="abs" style="left:196px;top:10px" width="50" height="40" viewBox="0 0 50 40"><rect x="1" y="1" width="48" height="38" fill="none" stroke="#bbb" stroke-width="2"/><polyline points="1,1 25,22 49,1" fill="none" stroke="#bbb" stroke-width="2"/></svg>
    <h3>NEWSLETTER SIGNUP</h3>
    <div class="field">Email Address</div>
    <div class="submit">SUBMIT</div>
  </div>
</aside>

<section class="partners" aria-label="Association memberships">
  <div class="badge" style="left:185px;top:53px;width:52px;height:62px"></div>
  <div class="badge" style="left:274px;top:54px;width:114px;height:58px;background:none;border:3px solid #333"></div>
  <div class="badge" style="left:416px;top:60px;width:102px;height:48px;background:#555"></div>
  <div class="badge" style="left:560px;top:50px;width:72px;height:66px;border-radius:50%;background:none;border:3px solid #333"></div>
  <div class="badge" style="left:677px;top:56px;width:49px;height:52px"></div>
  <div class="badge" style="left:770px;top:64px;width:46px;height:40px"></div>
  <div class="badge" style="left:856px;top:63px;width:96px;height:41px;background:#444"></div>
</section>

<footer class="site-footer">
  <h4 class="foot-head" style="left:178px;width:300px;font-weight:400">QUICKLINKS</h4>
  <ul class="foot-links" style="left:178px"><li>Home</li><li>Auctions</li><li>Real estate listings</li><li>Buyers</li></ul>
  <ul class="foot-links" style="left:385px"><li>Sellers</li><li>About us</li><li>Contact us</li><li>Brokers</li></ul>
  <h4 class="foot-head" style="left:564px;width:200px;font-weight:400">INFORMATION</h4>
  <ul class="foot-links" style="left:564px"><li>FAQ</li><li>Sitemap</li><li>Privacy Policy</li><li>Terms &amp; Condition</li></ul>
  <div class="foot-brand">
    <div class="name">Prairie Crest</div>
    <div class="sub">Valmond<br>Auction/Realty, LLC</div>
  </div>
  <div class="foot-social"><span></span><span></span><span></span><span></span></div>
</footer>
<div class="copyright">Copyright 2014 · All rights reserved</div>

</body>
</html>
```